Legal Journal cover - modern and sylish

We require a cover design for a new, modern and digital legal academic journal. Attached is our logo so you can get an idea of the feel. This academic journal will have several editions per year.Requirements for the cover design:-The feel of the cover is to be modern -In harmony with our logo-While staying uniform and set in its design,
Updates

Colors
ec1f27

Requirements
Must have
• 1) Colour. Each edition will use different colours. (So we will need the source files to be able to continue to do this)
• 2) An image section. We would like to be able to put in different image or photo with each edition. So we need to have a section, most likely in the shape of a strip, that can include a different image or photo each edition. This part is where we can put a different image in for each edition. So this section would need to be able to accommodate different types of images. It could be a single square. Or it could be a line (a strip) that an image or images.
• 3) A title for the edition and volume and number. Like this:
• Volume 34, No 2 (2016): Contemporary Issues in Criminal Law
• I have attached a range of journals I found online to serve as inspiration.

```html
<!DOCTYPE html>
<html lang="en">
<head>
<meta charset="utf-8">
<title>Juris Nova Review — No 1, 2019</title>
<link rel="stylesheet" href="https://fonts.googleapis.com/css2?family=Arimo:wght@400;700&family=Roboto+Condensed:wght@700&display=swap">
<style>
  :root {
    --cover-red: #ec1f27;
    --paper: #ffffff;
    --ink: #1c1414;
    --title-shadow: rgba(80, 0, 0, 0.85);
    --frame: #3a1010;
  }
  * { margin: 0; padding: 0; box-sizing: border-box; }
  html, body {
    width: 848px; height: 1200px; overflow: hidden;
    background: var(--paper);
  }
  .cover {
    position: relative;
    width: 848px; height: 1200px;
    background: var(--cover-red);
    border: 1px solid var(--frame);
    overflow: hidden;
    font-family: "Arimo", Arial, sans-serif;
  }

  /* Issue corner */
  .issue-corner {
    position: absolute; top: 0; right: 0;
    width: 212px; height: 206px;
    background: var(--paper);
    border-bottom-left-radius: 150px 200px;
  }
  .issue-number {
    position: absolute; top: 6px; left: 715px;
    display: flex; align-items: flex-end;
    font-family: "Roboto Condensed", "Arial Narrow", sans-serif;
    font-weight: 700; color: var(--cover-red); line-height: 1;
  }
  .issue-number .sign { font-size: 58px; margin-right: 8px; margin-bottom: 6px; }
  .issue-number .num { font-size: 122px; }
  .issue-year {
    position: absolute; top: 106px; left: 713px;
    font-family: "Roboto Condensed", "Arial Narrow", sans-serif;
    font-weight: 700; font-size: 62px; line-height: 1;
    color: var(--cover-red);
  }

  /* Image strip */
  .strip-rails { position: absolute; top: 7px; left: 0; width: 260px; height: 1180px; }
  .strip-rails span {
    position: absolute; top: 0; bottom: 0; width: 3px;
    background: var(--paper);
  }
  .strip-rails span:nth-child(1) { left: 71px; }
  .strip-rails span:nth-child(2) { left: 104px; }
  .strip-rails span:nth-child(3) { left: 138px; }
  .strip-rails span:nth-child(4) { left: 173px; }
  .strip-rails span:nth-child(5) { left: 212px; }

  .masthead {
    position: absolute; top: 25px; left: 53px;
    width: 189px; height: 72px;
    background: var(--paper);
    display: flex; flex-direction: column; align-items: center; justify-content: center;
  }
  .masthead .name {
    font-family: "Arimo", Arial, sans-serif;
    font-weight: 700; font-size: 19px; line-height: 22px; letter-spacing: 0.5px;
    color: var(--cover-red); text-align: center;
  }

  .strip-photo {
    position: absolute; left: 53px;
    width: 189px; height: 237px;
  }
  .photo-machinery { top: 128px; background: linear-gradient(160deg, #6f7a5a 0%, #8c8f86 40%, #6b6a63 75%, #4c4a42 100%); }
  .photo-tower     { top: 395px; background: linear-gradient(180deg, #5a6fc0 0%, #8c9bd8 50%, #5b71c9 100%); }
  .photo-silos     { top: 662px; background: linear-gradient(180deg, #c9c7b8 0%, #e8dfa6 45%, #d8b846 75%, #6a5a3c 100%); }
  .photo-offices   { top: 929px; background: linear-gradient(180deg, #5a86d6 0%, #e9eef4 35%, #9aa6b6 60%, #5f7d47 80%, #7d7f7a 100%); }

  /* Title */
  .journal-title {
    position: absolute; top: 150px; left: 300px;
    font-family: "Arimo", Arial, sans-serif;
    font-weight: 700; font-size: 118px; line-height: 145px;
    color: var(--paper);
    text-shadow: 7px 7px 5px var(--title-shadow);
    letter-spacing: -1px;
  }
  .journal-title span { display: block; }

  /* Lead text */
  .lead {
    position: absolute; left: 300px; width: 300px;
    font-size: 18px; line-height: 22.3px;
    color: var(--ink);
  }
  .lead-1 { top: 622px; }
  .lead-2 { top: 778px; }
  .lead-3 { top: 934px; }
  .lead-4 { top: 978px; }
</style>
</head>
<body>
  <main class="cover">
    <div class="issue-corner"></div>
    <div class="issue-number"><span class="sign">№</span><span class="num">1</span></div>
    <div class="issue-year">2019</div>

    <div class="strip-rails" aria-hidden="true">
      <span></span><span></span><span></span><span></span><span></span>
    </div>

    <div class="masthead">
      <span class="name">JURIS NOVA</span>
      <span class="name">REVIEW</span>
    </div>

    <div class="strip-photo photo-machinery" role="img" aria-label="Photo of old industrial machinery with valves and a pressure gauge"></div>
    <div class="strip-photo photo-tower" role="img" aria-label="Photo of a steel lattice tower against a blue sky"></div>
    <div class="strip-photo photo-silos" role="img" aria-label="Photo of tall industrial silos with a stair tower"></div>
    <div class="strip-photo photo-offices" role="img" aria-label="Photo of a modern office building with landscaped grounds"></div>

    <h1 class="journal-title"><span>JURIS</span><span>NOVA</span><span>REVIEW</span></h1>

    <p class="lead lead-1">Lorem ipsum dolor sit amet,<br>consectetur meri odipiscing elit<br>Mauris pretium porta turpis,<br>semper ornare magna elementum<br>convallis.</p>
    <p class="lead lead-2">Nulla lorem eros, hendrerit a mattis<br>vel, elementum aliquam nisi. Etiam<br>vel sapien mi. Cros nec varius<br>ipsum. Interdum et malesuada<br>fames ac ante ipsum primis in<br>faucibus.</p>
    <p class="lead lead-3">Proin euismod lobortis lacinia.</p>
    <p class="lead lead-4">Vestibulum velit volutpat dolor<br>tristique fermentum. Etiam<br>commodo, lacus enim lacinla lorem<br>urna sit amet nibh.</p>
  </main>
</body>
</html>
```